Banner Ad Design Project -Oil and Gas Value Chain

I am needing to create a simple graphic like the one here:

size: 720x300
http://craftpanelhub.example/designresources/banners/examples/720x300.php

Oil and Gas Value Chain:
The oil industry has three levels: upstream, midstream, and downstream which encompass the main segments in the supply chain. The upstream level includes the exploration, drilling, and production of crude oil and the midstream level includes the transportation and trading of crude oil to refineries. The downstream level refers to the refining of crude oil into finished product, the storage of crude oil, and the distribution and marketing of crude oil to wholesalers and retailers.

http://www.fuelvistaplan.example/images/value_chain.gif
http://www.crudelearnhub.example/modules/m008/imgs/fig_001.jpg
Here is another that is more for reference:

http://www.halvern.example/web/soc142/team9/GVC_clip_image002.jpg

https://www.findora.example/search?q=oil+value+chain&hl=en&tbo=u&prmd=imvns&tbm=isch&source=univ&sa=X&ei=I1hsUOuEC-SK2wXry4DAAg&ved=0CDMQsAQ&biw=1680&bih=925

```html
<!DOCTYPE html>
<html lang="en">
<head>
<meta charset="utf-8">
<title>Oil and Gas Value Chain</title>
<link href="https://fonts.googleapis.com/css2?family=Bebas+Neue&family=Oswald:wght@600;700&display=swap" rel="stylesheet">
<style>
  :root {
    --page: #ffffff;
    --panel-top: #f4f4f4;
    --panel-bottom: #e9e9e9;
    --ink: #2b2b2b;
    --teal: #1c7c99;
    --blue: #1a6fb8;
    --pill-top: #5c5c5c;
    --pill-bottom: #161616;
    --divider: #b9b9b9;
    --tick: #6cbf2a;
  }
  * { box-sizing: border-box; margin: 0; padding: 0; }
  html, body { width: 1200px; height: 900px; overflow: hidden; background: var(--page); }
  body { position: relative; font-family: "Oswald", "Arial Narrow", sans-serif; color: var(--ink); }

  .banner {
    position: absolute; left: 60px; top: 225px; width: 1080px; height: 450px;
    background: linear-gradient(180deg, var(--panel-top), var(--panel-bottom));
    box-shadow: 0 6px 30px rgba(0,0,0,.45);
  }
  .banner-title {
    position: absolute; top: 28px; left: 0; width: 100%; text-align: center;
    font-weight: 700; font-size: 38px; letter-spacing: 4px; line-height: 1;
  }
  .header-band {
    position: absolute; top: 80px; left: 0; width: 100%; height: 60px;
    border-bottom: 1px solid #d6d6d6;
    box-shadow: 0 6px 8px -6px rgba(0,0,0,.18);
  }
  .stage-head {
    position: absolute; top: 88px; display: flex; align-items: center; gap: 14px;
    font-weight: 700; font-size: 35px; color: var(--teal); line-height: 1; letter-spacing: 2px;
    white-space: nowrap;
  }
  .stage-num {
    width: 33px; height: 33px; background: #1c1c1c; color: #fff; font-size: 26px; letter-spacing: 0;
    display: flex; align-items: center; justify-content: center; border-radius: 2px;
  }
  .divider {
    position: absolute; top: 93px; bottom: 0; width: 0;
    border-left: 1px dashed var(--divider);
  }
  .pill {
    position: absolute; height: 35px; border-radius: 6px;
    background: linear-gradient(180deg, var(--pill-top), var(--pill-bottom));
    color: #fff; font-family: "Bebas Neue", "Arial Narrow", sans-serif;
    font-size: 24px; line-height: 37px; text-align: center; white-space: nowrap;
    box-shadow: 0 2px 3px rgba(0,0,0,.35); letter-spacing: .3px;
  }
  .step-arrow { position: absolute; width: 24px; height: 24px; }
  .stage-arrow { position: absolute; width: 48px; height: 48px; }

  .down-list { position: absolute; left: 720px; top: 150px; width: 360px; }
  .down-item {
    margin: 0 30px; text-align: center; white-space: nowrap;
    font-family: "Bebas Neue", "Arial Narrow", sans-serif; font-size: 26px;
    line-height: 45px; text-transform: uppercase;
  }
  .down-item.highlight { color: var(--teal); }
  .down-item + .down-item { border-top: 1px dashed #9a9a9a; }
  .tick { position: absolute; width: 30px; height: 26px; }
</style>
</head>
<body>
  <section class="banner">
    <h1 class="banner-title">OIL AND GAS VALUE CHAIN:</h1>
    <div class="header-band"></div>

    <div class="stage-head" style="left:15px"><span class="stage-num">1</span>UPSTREAM</div>
    <div class="stage-head" style="left:375px"><span class="stage-num">2</span>MIDSTREAM</div>
    <div class="stage-head" style="left:735px"><span class="stage-num">3</span>DOWNSTREAM</div>

    <div class="divider" style="left:360px"></div>
    <div class="divider" style="left:720px"></div>

    <!-- Upstream -->
    <div class="pill" style="left:50px; top:175px; width:253px">EXPLORATION</div>
    <svg class="step-arrow" style="left:164px; top:228px" viewBox="0 0 24 24"><circle cx="12" cy="12" r="12" fill="var(--blue)"/><path d="M7 9 L12 17 L17 9 L12 12 Z" fill="none" stroke="#fff" stroke-width="1.6" stroke-linejoin="round"/></svg>
    <div class="pill" style="left:50px; top:270px; width:253px">DRILLING</div>
    <svg class="step-arrow" style="left:164px; top:326px" viewBox="0 0 24 24"><circle cx="12" cy="12" r="12" fill="var(--blue)"/><path d="M7 9 L12 17 L17 9 L12 12 Z" fill="none" stroke="#fff" stroke-width="1.6" stroke-linejoin="round"/></svg>
    <div class="pill" style="left:41px; top:366px; width:267px">PRODUCTION OF CRUDE OIL</div>

    <!-- Midstream -->
    <div class="pill" style="left:414px; top:175px; width:252px">TRANSPORTATION</div>
    <svg class="step-arrow" style="left:528px; top:228px" viewBox="0 0 24 24"><circle cx="12" cy="12" r="12" fill="var(--blue)"/><path d="M7 9 L12 17 L17 9 L12 12 Z" fill="none" stroke="#fff" stroke-width="1.6" stroke-linejoin="round"/></svg>
    <div class="pill" style="left:380px; top:270px; width:322px">TRADING OF CRUDE OIL TO REFINERIES</div>

    <!-- Stage arrows -->
    <svg class="stage-arrow" style="left:336px; top:208px" viewBox="0 0 48 48"><circle cx="24" cy="24" r="23" fill="var(--blue)" stroke="#fff" stroke-width="2"/><path d="M16 15 L34 24 L16 33 L21 24 Z" fill="none" stroke="#fff" stroke-width="2.4" stroke-linejoin="round"/></svg>
    <svg class="stage-arrow" style="left:695px; top:208px" viewBox="0 0 48 48"><circle cx="24" cy="24" r="23" fill="var(--blue)" stroke="#fff" stroke-width="2"/><path d="M16 15 L34 24 L16 33 L21 24 Z" fill="none" stroke="#fff" stroke-width="2.4" stroke-linejoin="round"/></svg>

    <!-- Downstream -->
    <div class="down-list">
      <svg class="tick" style="left:37px; top:37px" viewBox="0 0 30 26"><path d="M3 14 L11 22 L27 4" fill="none" stroke="var(--tick)" stroke-width="5" stroke-linecap="round" stroke-linejoin="round"/></svg>
      <svg class="tick" style="left:27px; top:99px" viewBox="0 0 30 26"><path d="M3 14 L11 22 L27 4" fill="none" stroke="var(--tick)" stroke-width="5" stroke-linecap="round" stroke-linejoin="round"/></svg>
      <svg class="tick" style="left:27px; top:187px" viewBox="0 0 30 26"><path d="M3 14 L11 22 L27 4" fill="none" stroke="var(--tick)" stroke-width="5" stroke-linecap="round" stroke-linejoin="round"/></svg>
      <div class="down-item">Refining of crude oil<br>into finished product</div>
      <div class="down-item highlight">The storage of crude oil</div>
      <div class="down-item">The distribution and<br>marketing of crude oil<br>to wholesalers and retailers</div>
    </div>
  </section>
</body>
</html>
```